Q7 Teaser

One page teaser for our business information and model. A financial service SPV platform.

Target Market(s)

Financial Professionals

Industry/Entity Type

Financial Service

Font styles to use
Sans Serif

Colors
ffcf3e
ffffff
cfcfcf
9d9d9d
aaaaaa
fbed22
ffc214
fee18a
fbee3f

Requirements
Must have
• Unique appearance of USPs.
• Important claims: Low Cost. First Class.
• and: We liberate the buy-side from the sell-side
Nice to have
• maybe keyword cloud

```html
<!DOCTYPE html>
<html lang="en">
<head>
<meta charset="utf-8">
<title>QSeven Teaser</title>
<link rel="stylesheet" href="https://fonts.googleapis.com/css2?family=Open+Sans:wght@300;400;600;700&family=Roboto+Condensed:wght@400;700&display=swap">
<style>
  :root{
    --stage:#e6e6e6;
    --blue-deep:#4a68a6;
    --blue-mid:#7f93bf;
    --mist:#cfd2d9;
    --grey-soft:#c6c8cc;
    --ink:#222222;
    --text-grey:#555555;
    --heading-grey:#6b6b6b;
    --gold:#cc9936;
    --gold-text:#c8922a;
    --gold-light:#d9a94a;
    --cream:#f7eedd;
    --white:#ffffff;
  }
  *{margin:0;padding:0;box-sizing:border-box}
  html,body{width:1200px;height:1200px;overflow:hidden;background:var(--stage)}
  body{font-family:"Open Sans",sans-serif;position:relative}
  .page{
    position:absolute;left:176px;top:0;width:938px;height:1328px;
    transform:scale(0.9036);transform-origin:top left;
    background:var(--white);overflow:hidden;
  }
  .hero{
    position:absolute;left:0;top:0;width:938px;height:969px;
    background:
      radial-gradient(ellipse 70% 55% at 80% 72%, rgba(255,255,255,.95), rgba(255,255,255,0) 70%),
      linear-gradient(172deg, var(--blue-deep) 0%, var(--blue-mid) 30%, var(--mist) 52%, #e4e5e8 72%, var(--grey-soft) 100%);
  }
  .hero-photo{
    position:absolute;left:240px;top:-153px;width:680px;height:680px;border-radius:50%;
    background:
      radial-gradient(circle at 70% 30%, rgba(200,215,240,.55), rgba(0,0,0,0) 45%),
      linear-gradient(150deg,#1c2a48 0%,#33476f 45%,#7f8fb0 80%,#c3cad8 100%);
  }
  .headline{
    position:absolute;left:97px;top:160px;color:var(--white);
    font-weight:300;font-size:82px;line-height:85px;letter-spacing:-1.5px;
  }
  .intro{
    position:absolute;left:95px;top:553px;width:376px;
    font-weight:300;font-size:16.1px;line-height:25.2px;color:var(--text-grey);
  }
  .claim{
    position:absolute;left:508px;top:553px;width:380px;text-align:center;
    font-weight:600;font-size:36px;line-height:37px;color:var(--heading-grey);
  }
  .usp-box{
    position:absolute;left:501px;top:689px;width:400px;height:280px;
    background:var(--cream);border-radius:32px 32px 0 0;
    display:flex;justify-content:space-around;padding:33px 6px 0;
  }
  .usp-col{display:flex;flex-direction:column;gap:10px;text-align:center;width:190px}
  .usp{font-size:13.6px;line-height:15.5px;font-weight:700;color:var(--ink)}
  .usp.accent{color:var(--gold-text)}
  .pricing-band{
    position:absolute;left:0;top:969px;width:938px;height:85px;background:var(--gold);
    color:var(--white);font-family:"Roboto Condensed",sans-serif;font-size:18.5px;
    line-height:23px;padding-top:17px;text-align:center;padding-left:10px;
  }
  .keyword-panel{
    position:absolute;left:0;top:1054px;width:285px;height:170px;
    background:linear-gradient(135deg,var(--gold) 0%,var(--gold-light) 100%);
    border-radius:0 0 44px 0;
  }
  .brand-name{
    position:absolute;left:440px;top:1100px;
    font-weight:600;font-size:54px;line-height:70px;color:var(--gold);
  }
  .tagline{
    position:absolute;left:317px;top:1200px;font-weight:700;font-size:16.5px;
    letter-spacing:4.6px;color:var(--gold);
  }
  .contact{
    position:absolute;left:0;top:1237px;width:938px;text-align:center;
    font-weight:600;font-size:14.3px;color:var(--ink);
  }
  .about{
    position:absolute;left:0;top:1264px;width:938px;text-align:center;
    font-weight:300;font-size:11.6px;line-height:15px;color:var(--text-grey);
  }
</style>
</head>
<body>
  <main class="page">
    <section class="hero">
      <div class="hero-photo" role="img" aria-label="Photo of a businessman touching a glowing stock market candlestick chart"></div>
      <h1 class="headline">We liberate<br>the buy-side<br>from the<br>sell-side</h1>
      <p class="intro">We serve our clients with the power to create their own branded, tailor-made financial products and investment solutions by providing them with right tools and structures to establish and operate first class off-balance sheet issuance vehicles (SPV). We create unique solutions to expand your business reach, services and qualities by liberating financial product issuance to buy-side. Asset owners, distributers and managers are given the full capability to securitise their own asset base in unlimited capacity, outside their balance sheet with customisable transparency and counterparty risk. A clear and simple solution to serve your best interests and without the need for conventional sell-side issuers.</p>
      <h2 class="claim">We democratise structured financial product issuance</h2>
      <div class="usp-box">
        <div class="usp-col">
          <div class="usp accent">Off-balance sheet</div>
          <div class="usp">Own issuance vehicle<br>(SPV)</div>
          <div class="usp accent">Regulatory compliant<br>(MIFID)</div>
          <div class="usp">Swiss Paying Agent</div>
          <div class="usp accent">Various<br>off-shore locations</div>
          <div class="usp">Open Architecture</div>
          <div class="usp accent">Daily Liquidity</div>
        </div>
        <div class="usp-col">
          <div class="usp accent">Customised<br>Transparency</div>
          <div class="usp">Low cost structure</div>
          <div class="usp accent">Your own fee policy</div>
          <div class="usp">Investment<br>&amp; risk control</div>
          <div class="usp accent">Quick setup</div>
          <div class="usp">Transparent<br>secondary market</div>
          <div class="usp accent">Full transparent pricing</div>
        </div>
      </div>
    </section>

    <div class="pricing-band">
      Establishment Cost CHF 20’000 &nbsp;&nbsp;|&nbsp;&nbsp; Recurring Cost Yearly 20 BPS (&gt; CHF 20’000) &nbsp;&nbsp;|&nbsp;&nbsp; Product Cost &nbsp;CHF 2’000<br>
      Ticket Fee for Adjustments, Corporate Actions &amp; Rebalancing &nbsp;-&nbsp; Documentation Standard Set inkl. KID
    </div>

    <div class="keyword-panel" role="img" aria-label="Decorative word cloud of structured product types"></div>

    <div class="brand-name">QSeven</div>
    <p class="tagline">YOUR BRAND. YOUR REWARD. YOUR SOLUTION.</p>

    <p class="contact">QSeven Financial Products AG &nbsp;I&nbsp; Talgasse 14 &nbsp;I&nbsp; CH-8004 Zürich &nbsp;I&nbsp; www.qsevenfp.com &nbsp;I&nbsp; +41 44 000 12 34</p>
    <p class="about">QSeven Financial Product AG is a financial service provider built on the unique experience and robust track record<br>of its team. Our founders gathered the most qualified experts to benefit our clients and business partners.</p>
  </main>
</body>
</html>
```